business card design for a plumbing contractor

i need a double business card for a plumbing business, our initial service is residential Sewer Drain Cleaning.

Target Market(s)

other plumbing Business

Industry/Entity Type

Plumbing

Contact Information for Business Card

www.PipeworksCrestline.example- 5817302946-

Font styles to use
Serif

Colors
ec1f27
0455a3

```html
<!DOCTYPE html>
<html lang="en">
<head>
<meta charset="utf-8">
<title>Pipeworks Crestline – Business Card</title>
<link href="https://fonts.googleapis.com/css2?family=Jost:wght@400;500;700&display=swap" rel="stylesheet">
<style>
  :root {
    --brand-red: #ec1f27;
    --brand-blue: #0455a3;
    --paper: #ffffff;
    --logo-grey: #6e655c;
    --stage: #111214;
  }
  html, body {
    margin: 0;
    padding: 0;
    width: 1200px;
    height: 1074px;
    overflow: hidden;
    background: var(--stage);
    font-family: "Jost", "Futura", sans-serif;
  }
  .canvas {
    position: relative;
    width: 1200px;
    height: 1074px;
  }
  .card {
    position: absolute;
    left: 250px;
    width: 700px;
    height: 400px;
    box-shadow: 0 10px 30px rgba(0,0,0,0.6);
  }
  .card--back { top: 90px; }
  .card--front { top: 584px; }
  .card svg { display: block; width: 700px; height: 400px; }
  .logo-name {
    font-family: "Jost", sans-serif;
    font-weight: 700;
    fill: var(--logo-grey);
  }
  .tagline {
    font-weight: 500;
    font-size: 18px;
    letter-spacing: 1px;
    fill: var(--paper);
  }
  .holder-name {
    font-weight: 500;
    font-size: 26px;
    letter-spacing: 1.5px;
    fill: var(--brand-blue);
  }
  .holder-role {
    font-size: 15px;
    fill: var(--brand-red);
    letter-spacing: 0.5px;
  }
  .contact {
    font-size: 17px;
    fill: var(--paper);
  }
  .contact-label { font-weight: 700; }
</style>
</head>
<body>
<main class="canvas">

  <section class="card card--back" aria-label="Business card back">
    <svg viewBox="0 0 700 400" xmlns="http://www.w3.org/2000/svg">
      <rect class="card-paper" width="700" height="400" fill="var(--paper)"/>
      <path class="wave-red" d="M0,130 C160,110 260,150 360,230 C470,315 590,330 700,320 V400 H0 Z" fill="var(--brand-red)"/>
      <g class="brand-mark">
        <rect x="230" y="106" width="26" height="26" fill="var(--brand-red)"/>
        <text class="logo-name" x="268" y="130" font-size="32">Pipeworks Crestline</text>
      </g>
      <text class="tagline" x="290" y="332" text-anchor="middle">SEWER DRAIN CLEANING, MAINTENANCE,</text>
      <text class="tagline" x="290" y="360" text-anchor="middle">TRENCHLESS PIPE INSTALLS.</text>
    </svg>
  </section>

  <section class="card card--front" aria-label="Business card front">
    <svg viewBox="0 0 700 400" xmlns="http://www.w3.org/2000/svg">
      <rect class="card-paper" width="700" height="400" fill="var(--paper)"/>
      <path class="wave-red" d="M0,70 C50,60 70,230 260,268 C390,295 430,340 465,400 H0 Z" fill="var(--brand-red)"/>
      <path class="wave-blue" d="M0,100 C70,100 95,255 265,288 C375,310 410,350 440,400 H0 Z" fill="var(--brand-blue)"/>
      <g class="brand-mark">
        <rect x="70" y="52" width="22" height="22" fill="var(--brand-red)"/>
        <text class="logo-name" x="102" y="72" font-size="27">Pipeworks Crestline</text>
      </g>
      <g class="holder">
        <text class="holder-name" x="660" y="196" text-anchor="end">DANIEL HARTWELL</text>
        <line x1="400" y1="212" x2="498" y2="212" stroke="var(--brand-red)" stroke-width="1.5"/>
        <text class="holder-role" x="660" y="217" text-anchor="end">Maintenance Manager</text>
      </g>
      <g class="contacts">
        <text class="contact" x="40" y="310"><tspan class="contact-label">T:</tspan> 5817302946</text>
        <text class="contact" x="40" y="340"><tspan class="contact-label">E:</tspan> Dispatcher@PipeworksCrestline.example</text>
        <text class="contact" x="40" y="370"><tspan class="contact-label">W:</tspan> www.PipeworksCrestline.example</text>
      </g>
    </svg>
  </section>

</main>
</body>
</html>
```